Law Firm Needs Brochure Redesign Using New Logo

We are a personal injury law firm that does auto injuries and other personal injury cases. We want a new brochure that has our updated logo and information. Instead of gold and black, we want more navy, as matches the new logo. The Auto Liability portion should read: "(required by the state of Arizona in the amounts of $25,000 per person / $50,000 per accident, but a higher amount may be best )." The other information can remain the same. We'd like the brochure to keep the same professional tone as the previous brochure.
Our website is https://www.marbrenlegal.com/.

```html
<!DOCTYPE html>
<html lang="en">
<head>
<meta charset="utf-8">
<title>Marbren Legal – Car Accident Brochure</title>
<link rel="stylesheet" href="https://fonts.googleapis.com/css2?family=Cinzel:wght@400;600;700&family=Libre+Baskerville&family=Source+Sans+3:ital,wght@0,400;0,600;0,700;1,400;1,600&display=swap">
<style>
  :root {
    --navy: #0e1b3a;
    --navy-deep: #0a1530;
    --blue: #1f6ea6;
    --blue-bright: #2f8fd0;
    --ink: #1c2130;
    --paper: #ffffff;
    --mist: #eef0f3;
    --backdrop: #d9dbde;
  }
  * { box-sizing: border-box; margin: 0; padding: 0; }
  html, body { width: 1200px; height: 900px; overflow: hidden; }
  body {
    background: var(--backdrop);
    font-family: "Source Sans 3", "Helvetica Neue", Arial, sans-serif;
    color: var(--ink);
    position: relative;
  }
  .spread, .cover {
    position: absolute;
    top: 150px;
    height: 600px;
    box-shadow: 0 6px 18px rgba(0,0,0,.18);
  }
  .spread { left: 40px; width: 780px; display: flex; }
  .panel { position: relative; width: 260px; height: 600px; overflow: hidden; }
  .panel + .panel { border-left: 1px solid rgba(255,255,255,.08); }

  .heading {
    font-family: "Cinzel", "Times New Roman", serif;
    color: var(--paper);
    text-align: center;
    line-height: 1.15;
    letter-spacing: .5px;
  }
  .heading .lead { font-weight: 700; font-size: 15px; display: block; }
  .heading .sub { font-weight: 400; font-size: 15px; display: block; }

  .tips { list-style: none; }
  .tips li {
    position: relative;
    padding-left: 22px;
    font-size: 9.6px;
    line-height: 1.3;
    margin-bottom: 9px;
  }
  .tips li::before {
    content: "";
    position: absolute;
    left: 2px; top: 2px;
    width: 10px; height: 10px;
    background: currentColor;
    opacity: .9;
  }
  .tips .key { color: var(--blue-bright); font-weight: 600; }

  /* Panel 1 */
  .tips-panel .top {
    background: var(--navy);
    height: 372px;
    padding: 30px 18px 0 18px;
    color: #e4e8ef;
  }
  .tips-panel .top .heading { margin-bottom: 18px; }
  .tips-panel .top .tips li::before { background: #ffffff; }
  .tips-panel .bottom {
    height: 228px;
    background: linear-gradient(180deg, #f5f6f8 0%, #e4e6ea 70%, #cfd2d7 100%);
    padding: 22px 18px 0 18px;
    color: var(--navy);
  }
  .tips-panel .bottom .tips li::before { background: var(--navy); }
  .tips-panel .bottom strong { font-weight: 700; color: var(--navy); }
  .tips-panel .bottom .more { color: var(--blue); }

  /* Panel 2 */
  .coverage-panel .top {
    background: var(--navy);
    height: 372px;
    padding: 34px 18px 0 18px;
    color: #e4e8ef;
  }
  .coverage-panel .heading { margin-bottom: 16px; }
  .coverage-panel .tips li { margin-bottom: 10px; }
  .coverage-panel .tips li::before { background: #ffffff; }
  .photo { display: block; }
  .coverage-panel .photo {
    height: 228px;
    background: linear-gradient(160deg, #9aa0a6 0%, #c9ccd0 40%, #7e838a 75%, #4b4f56 100%);
  }

  /* Panel 3 */
  .safety-panel .photo {
    height: 332px;
    background: linear-gradient(100deg, #6a6e75 0%, #d9dbde 40%, #f1f1f2 65%, #c98c2f 80%, #a7adb5 100%);
  }
  .safety-panel .band {
    background: var(--blue);
    height: 182px;
    padding: 14px 18px 0 18px;
    color: #ffffff;
  }
  .safety-panel .band h3 {
    font-family: "Cinzel", "Times New Roman", serif;
    font-weight: 600;
    font-size: 13.5px;
    letter-spacing: .3px;
    margin-bottom: 5px;
  }
  .safety-panel .band p {
    font-size: 9.4px;
    font-style: italic;
    font-weight: 600;
    line-height: 1.3;
  }
  .safety-panel .band .tips li { font-style: italic; margin-bottom: 8px; }
  .safety-panel .band .tips li::before { background: #ffffff; }
  .contact-strip {
    background: var(--navy);
    height: 86px;
    text-align: center;
    color: #ffffff;
    padding-top: 20px;
  }
  .contact-strip .phone {
    font-family: "Cinzel", "Times New Roman", serif;
    font-size: 17px;
    letter-spacing: 1px;
  }
  .contact-strip .web {
    font-family: "Cinzel", "Times New Roman", serif;
    font-size: 10.5px;
    letter-spacing: 1.5px;
    margin-top: 4px;
    color: #dfe5ee;
    text-decoration: none;
    display: block;
  }

  /* Cover */
  .cover {
    left: 880px;
    width: 260px;
    background: var(--paper);
    overflow: hidden;
  }
  .cover .photo {
    position: absolute;
    top: 0; right: 0;
    width: 150px; height: 292px;
    background: linear-gradient(180deg, #e9ecef 0%, #cfd5dc 50%, #9aa4af 100%);
  }
  .brand {
    position: absolute;
    top: 40px; left: 16px;
    display: flex;
    align-items: center;
    gap: 8px;
    color: var(--navy);
  }
  .brand .mark { width: 16px; height: 16px; background: var(--navy); }
  .brand .name {
    font-family: "Cinzel", "Times New Roman", serif;
    font-weight: 700;
    font-size: 12px;
    line-height: 1.15;
    letter-spacing: 1px;
  }
  .headline {
    position: absolute;
    top: 318px; left: 0; width: 260px;
    text-align: center;
    color: var(--navy);
    font-family: "Libre Baskerville", "Times New Roman", serif;
    font-weight: 400;
  }
  .headline .small { font-size: 17px; display: block; }
  .headline .big {
    font-family: "Cinzel", "Times New Roman", serif;
    font-size: 36px; font-weight: 700; color: var(--blue);
    display: block; line-height: 1.05; letter-spacing: 1px;
  }
  .headline .mid { font-size: 16px; display: block; line-height: 1.25; }
  .headline .tagline {
    font-family: "Source Sans 3", Arial, sans-serif;
    font-style: italic;
    font-size: 10.5px;
    color: var(--ink);
    margin-top: 8px;
    display: block;
  }
  .cover .footer {
    position: absolute;
    bottom: 0; left: 0; width: 260px; height: 130px;
    background: var(--navy);
    color: #ffffff;
    text-align: center;
    padding-top: 36px;
  }
  .cover .footer .phone {
    font-family: "Cinzel", "Times New Roman", serif;
    font-size: 24px;
    letter-spacing: 1px;
  }
  .cover .footer .web {
    font-family: "Cinzel", "Times New Roman", serif;
    font-size: 11px;
    letter-spacing: 1.5px;
    color: #dfe5ee;
    text-decoration: none;
    display: block;
    margin-top: 8px;
  }
</style>
</head>
<body>

<section class="spread">
  <article class="panel tips-panel">
    <div class="top">
      <h2 class="heading"><span class="lead">TOP 10 TIPS</span><span class="sub">TO AVOID A CRASH</span></h2>
      <ul class="tips">
        <li><span class="key">Anyone making a left turn must wait for all oncoming traffic to clear before proceeding.</span> Yes, even if the light has turned yellow. Wait to be sure that all traffic has stopped.</li>
        <li><span class="key">When your light turns green,</span> check to be sure that no vehicles are entering the intersection late.</li>
        <li><span class="key">Allow plenty of room between you and the car in front of you.</span> Traffic can stop in an instant, even if you can't see anything ahead.</li>
        <li><span class="key">Avoid being distracted.</span> Teenagers are especially susceptible to losing focus if there are too many friends in the car.</li>
        <li><span class="key">Keep the volume of your radio down and never wear headphones.</span> Cars are very soundproof these days, but you need to be able to hear an ambulance or police siren.</li>
      </ul>
    </div>
    <div class="bottom" role="img" aria-label="Faded photo of a road surface behind the remaining tips">
      <ul class="tips">
        <li><strong>Be especially careful on the weekends and early morning hours.</strong></li>
        <li><strong>Don't speed.</strong> <span class="more">Speed is a factor in most crashes. Street lights are timed and the freeway has traffic. It's likely you won't get there much faster even if you do speed.</span></li>
        <li><strong>Don't drink and drive.</strong> <span class="more">Many cab companies offer a free service to get you home safe.</span></li>
        <li><strong>Use your turn signals.</strong> <span class="more">This gives an early warning to vehicles you may not be able to see.</span></li>
      </ul>
    </div>
  </article>

  <article class="panel coverage-panel">
    <div class="top">
      <h2 class="heading"><span class="sub">HAVE THE RIGHT</span><span class="lead">COVERAGE</span></h2>
      <ul class="tips">
        <li>Many people don't know about the different kinds of insurance available. In addition to health insurance, we suggest:</li>
        <li>Auto Liability (required by the state of Arizona in the amounts of $25,000 per person / $50,000 per accident, but a higher amount may be best ).</li>
        <li>Uninsured or Underinsured Motorist Coverage. This protects YOU when the other driver doesn't have insurance or not enough.</li>
        <li>Medical Payments Coverage. Up to $5,000 in coverage will be paid out to you no matter who is at fault in an accident and does not need to be reimbursed.</li>
        <li>Homeowners / Renters Insurance. Protects you in case of injuries on your property as well as damage to your home from covered events.</li>
      </ul>
    </div>
    <div class="photo" role="img" aria-label="Photo of a broken side mirror lying on the road after a car crash"></div>
  </article>

  <article class="panel safety-panel">
    <div class="photo" role="img" aria-label="Photo of a hand gripping the handle of a crutch"></div>
    <div class="band">
      <h3>MODEL SAFE BEHAVIOR</h3>
      <ul class="tips">
        <li>Always buckle up. Always put your children in car seats/boosters that are rated for their height and weight.</li>
      </ul>
      <h3>NEVER TEXT WHILE DRIVING</h3>
      <ul class="tips">
        <li>Studies have shown that texting while driving is as dangerous as driving intoxicated</li>
      </ul>
      <p>Show your children that no text is more important than your safety. It can wait.</p>
    </div>
    <div class="contact-strip">
      <div class="phone">(602) 555-0187</div>
      <a class="web" href="https://www.marbrenlegal.com/">www.marbrenlegal.com</a>
    </div>
  </article>
</section>

<section class="cover">
  <div class="photo" role="img" aria-label="Photo of an older man seated in a wheelchair by a bright window"></div>
  <div class="brand">
    <span class="mark"></span>
    <span class="name">MARBREN LEGAL<br>INJURY LAWYERS</span>
  </div>
  <h1 class="headline">
    <span class="small">Protect your</span>
    <span class="big">FAMILY</span>
    <span class="mid">in case of a<br>CAR ACCIDENT</span>
    <span class="tagline">A little knowledge and preparation go a long way</span>
  </h1>
  <div class="footer">
    <div class="phone">602-555-0142</div>
    <a class="web" href="https://www.marbrenlegal.com/">www.marbrenlegal.com</a>
  </div>
</section>

</body>
</html>
```